San Francisco Pet Care Non Profit

Business Card Design for non profit organization.
We are a mobile pet care team who supports and attends to pets whose owners are homeless. Thanks for your help and creativity.

Industry/Entity Type

Non Profit

Contact Information for Business Card

Miriam Loxley
President
2817 Harrow Street, #516
San Francisco, CA 94187
phone: 415-782-3946
fax: 415-718-4053
miriam@warmpawvan.org
website: warmpawvan.org
facebook: facebook.com/WarmPawVan

Font styles to use
Serif
Sans Serif

Colors

Designer to choose colors to be used in the design.

Requirements
Must have
• above details and attached logo

```html
<!DOCTYPE html>
<html lang="en">
<head>
<meta charset="utf-8">
<title>WarmPawVan Business Card</title>
<link href="https://fonts.googleapis.com/css2?family=Montserrat:wght@600;700;800&family=Poppins:wght@300;400;500&display=swap" rel="stylesheet">
<style>
  :root {
    --sky: #29a9e1;
    --ink: #1b1a1a;
    --card-dark: #1f1d1e;
    --paper: #ffffff;
    --backdrop: #5a5d60;
    --rule: #ffffff;
  }
  * { box-sizing: border-box; margin: 0; padding: 0; }
  html, body { width: 1200px; height: 874px; overflow: hidden; }
  body {
    background: var(--backdrop);
    display: flex;
    flex-direction: column;
    align-items: center;
    justify-content: center;
    gap: 40px;
    font-family: "Poppins", sans-serif;
  }
  .card {
    position: relative;
    width: 640px;
    height: 366px;
    border-radius: 26px;
    overflow: hidden;
    box-shadow: 0 14px 30px rgba(0,0,0,.35);
  }

  /* brand lockup */
  .brand { display: flex; align-items: center; gap: 16px; }
  .brand-dot {
    width: 62px; height: 62px; border-radius: 50%;
    background: var(--sky);
    flex: none;
  }
  .brand-text { display: flex; flex-direction: column; }
  .brand-name {
    font-family: "Montserrat", sans-serif;
    font-weight: 800;
    font-size: 46px;
    line-height: 1;
    color: var(--sky);
    letter-spacing: -0.5px;
  }
  .brand-tagline {
    font-family: "Montserrat", sans-serif;
    font-weight: 700;
    font-size: 17px;
    margin-top: 4px;
    align-self: flex-end;
  }

  /* back */
  .card-back { background: var(--card-dark); }
  .card-back .brand { position: absolute; left: 120px; top: 110px; }
  .card-back .brand-tagline { color: var(--paper); }
  .social {
    position: absolute; left: 0; right: 0; top: 268px;
    display: flex; justify-content: center; align-items: center; gap: 10px;
    color: var(--paper); font-size: 16px; font-weight: 300;
  }
  .social-dot { width: 24px; height: 24px; border-radius: 50%; background: var(--sky); }

  /* front */
  .card-front { background: var(--paper); }
  .card-front .brand { position: absolute; left: 150px; top: 40px; }
  .card-front .brand-tagline { color: var(--ink); }
  .band {
    position: absolute; left: 0; right: 0; top: 150px; height: 170px;
    background: var(--sky);
  }
  .person { position: absolute; left: 60px; top: 34px; width: 230px; text-align: right; }
  .person-name {
    font-family: "Montserrat", sans-serif; font-weight: 700; font-size: 30px; line-height: 1.1;
  }
  .person-name .first { color: var(--paper); }
  .person-name .last { color: var(--ink); }
  .person-role { color: var(--paper); font-size: 16px; font-weight: 400; }
  .divider {
    position: absolute; left: 318px; top: 20px; width: 2px; height: 88px;
    background: var(--rule);
  }
  .contacts { position: absolute; left: 342px; top: 16px; list-style: none; }
  .contacts li {
    display: flex; align-items: center; gap: 10px;
    color: var(--paper); font-size: 14.5px; font-weight: 300; line-height: 23px;
  }
  .contacts svg { width: 15px; height: 15px; flex: none; }
  .address {
    position: absolute; left: 0; right: 0; top: 128px;
    display: flex; justify-content: center; align-items: center; gap: 10px;
    color: var(--ink); font-size: 15px; font-weight: 400;
  }
  .address svg { width: 22px; height: 26px; }
</style>
</head>
<body>

  <section class="card card-back">
    <div class="brand">
      <span class="brand-dot"></span>
      <div class="brand-text">
        <span class="brand-name">WarmPawVan</span>
        <span class="brand-tagline">Mobile Pet Care Team</span>
      </div>
    </div>
    <div class="social">
      <span class="social-dot"></span>
      <span>/WarmPawVan</span>
    </div>
  </section>

  <section class="card card-front">
    <div class="brand">
      <span class="brand-dot"></span>
      <div class="brand-text">
        <span class="brand-name">WarmPawVan</span>
        <span class="brand-tagline">Mobile Pet Care Team</span>
      </div>
    </div>

    <div class="band">
      <div class="person">
        <div class="person-name"><span class="first">Miriam</span> <span class="last">Loxley</span></div>
        <div class="person-role">President</div>
      </div>
      <div class="divider"></div>
      <ul class="contacts">
        <li>
          <svg viewBox="0 0 16 16" fill="#fff"><path d="M3.5 1.5l2.5 0 1 3.5-1.6 1.2c.9 1.8 2.2 3.1 4 4l1.2-1.6 3.4 1v2.6c0 .9-.8 1.6-1.7 1.5C6.6 13.1 2.9 9.4 2 3.2 1.9 2.3 2.6 1.5 3.5 1.5z"/></svg>
          415-782-3946
        </li>
        <li>
          <svg viewBox="0 0 16 16" fill="#fff"><rect x="4" y="1.5" width="8" height="4"/><rect x="1.5" y="6" width="13" height="6" rx="1"/><rect x="4" y="10" width="8" height="4.5" fill="#fff" stroke="#29a9e1" stroke-width="1"/></svg>
          415-718-4053
        </li>
        <li>
          <svg viewBox="0 0 16 16"><rect x="1.5" y="3.5" width="13" height="9" fill="#fff"/><path d="M1.5 3.5l6.5 5 6.5-5" fill="none" stroke="#29a9e1" stroke-width="1.2"/></svg>
          miriam@warmpawvan.org
        </li>
        <li>
          <svg viewBox="0 0 16 16" fill="none" stroke="#fff" stroke-width="1.3"><circle cx="8" cy="8" r="6.3"/><ellipse cx="8" cy="8" rx="2.8" ry="6.3"/><path d="M1.7 8h12.6M2.8 4.8h10.4M2.8 11.2h10.4"/></svg>
          www.warmpawvan.org
        </li>
      </ul>
      <div class="address">
        <svg viewBox="0 0 22 26" fill="none" stroke="#1b1a1a" stroke-width="1.6"><path d="M11 19C7 14 5 11 5 8a6 6 0 0112 0c0 3-2 6-6 11z" fill="#fff"/><circle cx="11" cy="8" r="2.2"/><path d="M6 19.5c-3 .6-4 1.5-4 2.5 0 1.6 4 2.8 9 2.8s9-1.2 9-2.8c0-1-1-1.9-4-2.5"/></svg>
        2817 Harrow Street, #516, San Francisco, CA 94187
      </div>
    </div>
  </section>

</body>
</html>
```